Beyond the Hunt Product Labeling

We need a label design for a new product we are launching. We have developed a cooking bag that will cook your fish or game bird instantly. This is for the everyday fisherman and upland game hunter. This label will be printed on a thin sticker on the front of a Mylar Bag. The Mylar Bag is 9 1/2 x 12 inches. Inside the Mylar Bag is 3 cooking bags.
Target Market(s)
hunters and fishermen
Industry/Entity Type
Cooking
Font styles to use
Sans Serif
Colors
Designer to choose colors to be used in the design.
Requirements
Must have
- It must have "Beyond the Hunt" logo. It should have Scale and Plume. Scale and Plume is the type of seasoning. It must have a small place on the label for net weight. It must also have the wording "Contains: 3 Individual Cooking Bags Inside.
Nice to have
- I really like a topographical map in the background. I have attached several images with products like that. It could also be cool having the background of the bag with a tiger trout's scales. I attached some images of that too. Some other ideas I thought i have is having a picture of the bird and fish on the bag. There is an GIF attached that has a cool looking fish that did that. There is also an image of a Holvak product that did the same thing.

```html
<!DOCTYPE html>
<html lang="en">
<head>
<meta charset="utf-8">
<title>Beyond the Hunt – Scale &amp; Plume Label</title>
<link href="https://fonts.googleapis.com/css2?family=Roboto+Condensed:wght@400;700&display=swap" rel="stylesheet">
<style>
  :root {
    --page-bg: #f2f2f2;
    --bag-dark: #2b2b30;
    --bag-mid: #55565c;
    --bag-light: #c9cacd;
    --label-blue: #0a78bd;
    --band-navy: #07234f;
    --band-navy-deep: #021a3e;
    --band-sheen: #2e5a86;
    --badge-orange: #e8762a;
    --badge-light: #f09a56;
    --ink: #1b1b1b;
    --white: #ffffff;
    --pill-text: #0c2447;
    --art-feather: #b88a5c;
    --art-trout: #8a7f52;
    --art-water: #0e4f86;
  }
  * { margin: 0; padding: 0; box-sizing: border-box; }
  html, body {
    width: 1200px; height: 1000px; overflow: hidden;
    background: var(--page-bg);
    font-family: "Roboto Condensed", "Arial Narrow", sans-serif;
  }
  .canvas { position: relative; width: 1200px; height: 1000px; }

  .bag {
    position: absolute; left: 283px; top: 100px; width: 634px; height: 800px;
    background: linear-gradient(90deg, var(--bag-dark) 0%, var(--bag-mid) 30%, var(--bag-light) 50%, var(--bag-mid) 70%, var(--bag-dark) 100%);
  }
  .label {
    position: absolute; left: 48px; top: 48px; width: 538px; height: 704px;
    border-radius: 14px; overflow: hidden;
    background: var(--label-blue);
  }
  .center-band {
    position: absolute; left: 114px; top: 0; width: 307px; height: 100%;
    background: linear-gradient(90deg, var(--band-navy-deep) 0%, var(--band-navy) 25%, var(--band-sheen) 50%, var(--band-navy) 75%, var(--band-navy-deep) 100%);
  }
  .brand-name {
    position: absolute; left: 0; right: 0; top: 134px;
    text-align: center; color: var(--white);
    font-weight: 700; font-size: 34px; letter-spacing: 0.5px;
  }
  .badge { position: absolute; left: 72px; top: 188px; width: 394px; height: 258px; }
  .product-name {
    position: absolute; left: 72px; top: 240px; width: 394px;
    text-align: center; color: var(--ink);
    font-weight: 700; font-size: 74px; line-height: 68px;
  }
  .product-tagline {
    position: absolute; left: 72px; top: 376px; width: 394px;
    text-align: center; color: var(--ink);
    font-weight: 700; font-size: 20px;
  }
  .game-art {
    position: absolute; left: 122px; top: 444px; width: 290px; height: 150px;
    border-radius: 16px;
    background:
      linear-gradient(180deg, rgba(184,138,92,0.9) 0%, rgba(150,110,80,0.85) 40%, rgba(138,127,82,0.85) 62%, var(--art-water) 100%);
  }
  .audience {
    position: absolute; left: 0; right: 0; top: 612px;
    text-align: center; color: var(--badge-orange);
    font-size: 11px; letter-spacing: 0.2px;
  }
  .contents-pill {
    position: absolute; left: 98px; top: 636px; width: 342px; height: 34px;
    border-radius: 9px; background: var(--white);
    color: var(--pill-text); font-weight: 700; font-size: 17px;
    display: flex; align-items: center; justify-content: center;
  }
  .net-weight {
    position: absolute; left: 0; right: 0; top: 678px;
    text-align: center; color: var(--badge-orange);
    font-weight: 700; font-size: 12px;
  }
</style>
</head>
<body>
<main class="canvas">
  <section class="bag">
    <div class="label">
      <div class="center-band"></div>

      <div class="brand-name">BEYOND THE HUNT</div>

      <svg class="badge" viewBox="0 0 394 258" aria-hidden="true">
        <defs>
          <linearGradient id="badgeFill" x1="0" x2="1" y1="0" y2="0">
            <stop offset="0" stop-color="#e8762a"/>
            <stop offset="0.5" stop-color="#f09a56"/>
            <stop offset="1" stop-color="#e8762a"/>
          </linearGradient>
        </defs>
        <polygon points="197,2 390,58 390,196 197,256 4,196 4,58" fill="url(#badgeFill)"/>
        <polygon points="197,14 378,66 378,188 197,244 16,188 16,66" fill="none" stroke="#3a2410" stroke-width="1"/>
      </svg>
      <h1 class="product-name">SCALE &amp;<br>PLUME</h1>
      <p class="product-tagline">100% Natural Seasoning</p>

      <div class="game-art" role="img" aria-label="Pheasant standing above a trout in rippling water"></div>

      <p class="audience">FOR THE EVERYDAY FISHERMAN AND UPLAND GAME HUNTER</p>
      <div class="contents-pill">Contains: 3 Individual Cooking Bags Inside</div>
      <p class="net-weight">Net WT. 5.50 z</p>
    </div>
  </section>
</main>
</body>
</html>
```